Tervolan Pty Ltd professional business card

A professional business card template using the colours from the supplied logo.
Clean crisp lines while, Modern while not being over the top.

Target Market(s)

Construction, commerical and industrial

Industry/Entity Type

Communications

Contact Information for Business Card

For a Communications, IT, Optical fibre installation company

Colors
37b8a4

```html
<!DOCTYPE html>
<html lang="en">
<head>
<meta charset="utf-8">
<title>Tervolan Pty Ltd – Business Card</title>
<link rel="stylesheet" href="https://fonts.googleapis.com/css2?family=Montserrat:wght@400;500;700&display=swap">
<style>
  :root {
    --page-bg: #2a2a2a;
    --card-bg: #1c1c1d;
    --card-edge: #262627;
    --teal: #1b95a1;
    --white: #ffffff;
    --text-light: #e9e9e9;
  }
  * { box-sizing: border-box; margin: 0; padding: 0; }
  html, body { width: 1200px; height: 852px; overflow: hidden; }
  body {
    background: var(--page-bg);
    font-family: "Montserrat", sans-serif;
    position: relative;
  }
  .card {
    position: absolute;
    left: 280px;
    width: 640px;
    height: 366px;
    border-radius: 18px;
    background: linear-gradient(160deg, var(--card-edge), var(--card-bg) 60%);
    overflow: hidden;
    box-shadow: 0 10px 30px rgba(0,0,0,0.45);
  }
  .card--front { top: 30px; }
  .card--back { top: 456px; }

  .brand {
    display: flex;
    align-items: center;
    gap: 14px;
    color: var(--white);
    font-weight: 700;
    letter-spacing: 2px;
  }
  .brand__dot {
    width: 22px; height: 22px; border-radius: 50%;
    background: var(--teal);
  }
  .card--front .brand {
    position: absolute; left: 50%; top: 50%;
    transform: translate(-50%, -50%);
    font-size: 64px;
  }
  .card--back .brand {
    position: absolute; right: 40px; top: 50px;
    font-size: 50px;
  }
  .card--back .brand__dot { width: 18px; height: 18px; }

  .card__art { position: absolute; inset: 0; width: 100%; height: 100%; }

  .person { position: absolute; left: 40px; top: 152px; }
  .person__name {
    color: var(--teal); font-weight: 500; font-size: 22px; letter-spacing: 0.5px;
  }
  .person__role { color: var(--text-light); font-size: 15px; margin-top: 2px; }

  .contact { position: absolute; left: 40px; top: 222px; list-style: none; }
  .contact__item {
    display: flex; align-items: center; gap: 12px;
    color: var(--text-light); font-size: 16px; line-height: 25px;
  }
  .contact__item svg { width: 13px; height: 13px; fill: none; stroke: var(--teal); stroke-width: 2; }
  .contact__accent { color: var(--teal); }

  .address {
    position: absolute; right: 40px; top: 226px;
    text-align: right; color: var(--text-light); font-size: 15px; line-height: 22px;
  }
</style>
</head>
<body>
  <section class="card card--front">
    <div class="brand"><span class="brand__dot"></span>TERVOLAN</div>
  </section>

  <section class="card card--back">
    <svg class="card__art" viewBox="0 0 640 366" preserveAspectRatio="none" aria-hidden="true">
      <line x1="40" y1="206" x2="600" y2="206" stroke="var(--teal)" stroke-width="1.5"/>
      <path d="M0 366 L0 344 L380 344 C420 344 425 296 470 296 L640 296 L640 366 Z" fill="var(--teal)"/>
      <path d="M0 333 L372 333 C398 333 410 320 420 310" stroke="var(--white)" stroke-width="5" fill="none"/>
    </svg>

    <div class="brand"><span class="brand__dot"></span>TERVOLAN</div>

    <div class="person">
      <p class="person__name">MARCUS WHITFIELD</p>
      <p class="person__role">Director</p>
    </div>

    <ul class="contact">
      <li class="contact__item">
        <svg viewBox="0 0 16 16"><path d="M4 1 L6 5 L4.5 6.5 C5.5 9 7 10.5 9.5 11.5 L11 10 L15 12 L13.5 15 C7 15 1 9 1 2.5 Z"/></svg>
        (541) 208-3716
      </li>
      <li class="contact__item">
        <svg viewBox="0 0 16 16"><rect x="1.5" y="3.5" width="13" height="9"/><path d="M1.5 3.5 L8 9 L14.5 3.5"/></svg>
        info@tervolan.com
      </li>
      <li class="contact__item">
        <svg viewBox="0 0 16 16"><circle cx="8" cy="8" r="6.5"/><path d="M1.5 8 H14.5 M8 1.5 C5 5 5 11 8 14.5 M8 1.5 C11 5 11 11 8 14.5"/></svg>
        <span>www.<span class="contact__accent">tervolan</span>.com</span>
      </li>
    </ul>

    <p class="address">1187 Harlow Ridge<br>Dunmore, OR 97450</p>
  </section>
</body>
</html>
```